Accounting Practice Business Card Design

I have a logo I am happy for you to use in the design of the Business Card.
You can edit and change colours as you please, I am not fixated on it.
I am looking for a modern and clean overall feel for the finished design.

The business is a small accounting practice who thrives on word of mouth referrals and this card will be given to all current and prospect clients.

Industry/Entity Type

Accountant

Contact Information for Business Card

Marcus Elwin
Level 5, 8 Corvale Ridge Road
ASHGROVE RISE VIC 3187
Phone: 9481 3057
Email: melwin@mrfaccountants.com.au
Web: www.mrfaccountants.com.au

Font styles to use
Serif
Sans Serif

Colors
0555a3
3277b5
85acd3
0393ce
33a6d7
85cae6
00a990
33b8a4
9bcb3c

Requirements
Must have
• "The end to your tax problems begin with us"
• "A referral from you is our greatest compliment"
Nice to have
• Modern clean professional

```html
<!DOCTYPE html>
<html lang="en">
<head>
<meta charset="utf-8">
<title>MRF Accountants – Business Card</title>
<link rel="stylesheet" href="https://fonts.googleapis.com/css2?family=Jost:wght@400;500;600&family=Carlito&display=swap">
<style>
  :root {
    --brand-blue: #0f47f5;
    --brand-green: #8cff00;
    --card-border: #111111;
    --page-bg: #ffffff;
  }
  * { box-sizing: border-box; margin: 0; padding: 0; }
  html, body {
    width: 1200px; height: 1200px; overflow: hidden;
    background: var(--page-bg);
  }
  body { position: relative; font-family: "Jost", "Century Gothic", sans-serif; color: var(--brand-blue); }

  .stage {
    position: absolute; left: 0; top: 0;
    width: 1500px; height: 1500px;
    transform: scale(0.8); transform-origin: 0 0;
  }

  .card {
    position: absolute; left: 219px; width: 1066px;
    border: 2px solid var(--card-border); background: #fff; overflow: hidden;
  }
  .card--front { top: 95px; height: 581px; }
  .card--back { top: 841px; height: 580px; }

  .wordmark {
    position: absolute; left: 0; right: 0; text-align: center;
    font-family: "Jost", sans-serif; font-weight: 600; color: var(--brand-blue);
    letter-spacing: 1px; line-height: 1;
  }
  .card--front .wordmark { top: 52px; font-size: 60px; }
  .card--back .wordmark { top: 410px; font-size: 62px; }

  .name-band {
    position: absolute; left: 0; right: 2px; top: 177px; height: 92px;
    background: var(--brand-green); text-align: center;
  }
  .name-band__name {
    font-weight: 600; font-size: 56px; letter-spacing: -2px;
    line-height: 1; margin-top: 10px;
  }
  .name-band__role { font-family: "Jost", sans-serif; font-size: 28px; font-weight: 400; line-height: 1; margin-top: -6px; }

  .contact { position: absolute; left: 0; right: 0; text-align: center; font-size: 28px; font-weight: 400; line-height: 1; }
  .contact__label { font-family: "Jost", sans-serif; font-weight: 500; margin-right: 8px; }
  .address-line1 { top: 297px; }
  .address-line2 { top: 337px; }
  .phone { top: 398px; }
  .email { top: 442px; }
  .web { top: 485px; }

  .tagline-band {
    position: absolute; left: 0; right: 2px; bottom: 0; height: 38px;
    background: var(--brand-green); text-align: center;
    font-weight: 500; font-size: 28px; letter-spacing: -1px; line-height: 42px;
    padding-right: 30px;
  }

  .back-message {
    position: absolute; left: 0; right: 0; text-align: center;
    font-family: "Carlito", "Calibri", sans-serif; font-size: 54px; line-height: 60px;
    padding-right: 30px;
  }
  .back-message--referral { top: 58px; }
  .back-message--thanks { top: 248px; }
</style>
</head>
<body>
  <div class="stage">
    <section class="card card--front">
      <div class="wordmark">MRF Accountants</div>
      <div class="name-band">
        <div class="name-band__name">MARCUS ELWIN</div>
        <div class="name-band__role">accountant</div>
      </div>
      <p class="contact address-line1">Level 5, 8 Corvale Ridge Road</p>
      <p class="contact address-line2">ASHGROVE RISE VIC 3187</p>
      <p class="contact phone"><span class="contact__label">Phone:</span>9481 3057</p>
      <p class="contact email"><span class="contact__label">Email:</span>melwin@mrfaccountants.com.au</p>
      <p class="contact web"><span class="contact__label">Web:</span>www.mrfaccountants.com.au</p>
      <div class="tagline-band">THE END TO YOUR TAX PROBLEMS BEGIN WITH US</div>
    </section>

    <section class="card card--back">
      <p class="back-message back-message--referral">A refferal from you is our<br>greatest compliment</p>
      <p class="back-message back-message--thanks">Thank you for choosing us</p>
      <div class="wordmark">MRF Accountants</div>
    </section>
  </div>
</body>
</html>
```